Design a Website Mockup for simple help desk page

Hi,
We just signed up for a hosted support desk.
There we have access to a small header, and home page html, now this is hosted on help.brindlequay.com.. you can check our main site by put www, instead of support. we want the theme to match our design, and footer, remember the header banner is static, we need a sweet design matching for the support desk page, and once approved htmlized should be included. here is the screen shot. Should also have a fun stock photography of may be support team wearing shirts with our logos, please first look at our color theme etc on our main site, i will be selecting a winner soon as this is urgent
http://clipvantor.com/t/4KQrWZLMP32
The header image should contain your companies logo and anything else you wish to put on it. It will lay on top of the background image.
The header image should be 1138 pixels wide and the same height as the background.
Anything smaller than 1138 pixels wide will be centered across the top.

```html
<!DOCTYPE html>
<html lang="en">
<head>
<meta charset="utf-8">
<title>BrindleQuay Help Desk</title>
<link href="https://fonts.googleapis.com/css2?family=Arimo:wght@400;700&display=swap" rel="stylesheet">
<style>
:root{
  --brand:#a3254f;
  --ink:#333;
  --muted:#8a9aa0;
  --rule:#444;
  --page:#f1f1f1;
  --panel:#efefef;
  --band:#4a4a4a;
  --tab-accent:#2a9fd6;
}
*{box-sizing:border-box;margin:0;padding:0}
html,body{width:1200px;height:1068px;overflow:hidden}
body{position:relative;background:var(--page);font-family:"Arimo",Arial,sans-serif;color:var(--ink)}
.site-header{position:absolute;left:0;top:0;width:1200px;height:90px;background:#fff;border-bottom:3px solid var(--rule)}
.brand{position:absolute;left:116px;top:24px;display:flex;align-items:center;gap:10px}
.brand-dot{width:34px;height:34px;border-radius:50%;background:var(--brand)}
.brand-name{font-size:28px;color:var(--brand);font-weight:400}
.page-title{position:absolute;right:122px;top:24px;font-size:35px;color:var(--brand);font-weight:400}
.help-shell{position:absolute;left:93px;top:90px;width:1015px;height:706px;background:#fff;box-shadow:0 1px 3px rgba(0,0,0,.2)}
.tab-bar{position:absolute;left:0;top:0;width:100%;height:40px;background:#f4f4f4;border-bottom:1px solid #ddd}
.tab{position:absolute;top:0;height:40px;line-height:40px;font-size:13.5px;color:#555}
.tab.active{left:0;width:70px;background:#fff;border-top:3px solid var(--tab-accent);text-align:center;line-height:34px;font-weight:700;color:#222;height:41px}
.search{position:absolute;right:0;top:11px;width:225px;height:26px;border:1px solid #ccc;background:#fff;font-size:11px;color:#aaa;padding:6px 7px}
.support-panel{position:absolute;left:54px;top:101px;width:894px;height:509px;background:var(--panel);border:1px solid #ddd}
.panel-head{height:79px;background:linear-gradient(#cfcfcf,#b3b3b3);color:#fff;padding:20px 44px}
.panel-head h1{font-size:21px;font-weight:400;line-height:24px}
.panel-head p{font-size:15px;line-height:18px}
.options-card{position:absolute;left:18px;top:132px;width:856px;height:217px;background:#fff;border-radius:6px}
.agent-photo{position:absolute;left:2px;top:1px;width:154px;height:216px;background:linear-gradient(#e8dcd2,#c9b8a6)}
.option{position:absolute;top:26px;width:312px}
.option.question{left:183px}
.option.ticket{left:527px}
.pill{height:39px;line-height:39px;background:var(--brand);color:#fff;font-size:20px;border-radius:6px;padding-left:10px}
.option p{margin-top:22px;font-size:16px;line-height:21px;color:var(--muted)}
.btn{position:absolute;top:140px;height:31px;line-height:31px;background:var(--brand);color:#fff;font-size:19px;border-radius:8px;text-align:center}
.question .btn{left:0;width:179px}
.ticket .btn{left:1px;width:238px}
.footer-links{position:absolute;top:834px;font-size:9px;line-height:12.6px;color:#555;list-style:none}
.social-title{position:absolute;left:660px;top:834px;font-size:9px;font-weight:700;color:#555}
.social{position:absolute;top:856px;width:31px;height:31px;background:#bdbdbd;border-radius:3px;border:1px solid #aaa}
.to-top{position:absolute;left:1031px;top:834px}
.contact-band{position:absolute;left:0;top:932px;width:1200px;height:35px;background:var(--band);color:#fff;font-size:15px;display:flex;align-items:center;justify-content:center;gap:8px}
.contact-band a{color:#fff}
.copyright{position:absolute;left:0;top:967px;width:1200px;height:30px;background:#fff;text-align:center;font-size:9px;line-height:30px;color:var(--brand)}
</style>
</head>
<body>
<header class="site-header">
  <div class="brand"><span class="brand-dot"></span><span class="brand-name">BrindleQuay</span></div>
  <div class="page-title">Help Desk</div>
</header>

<main class="help-shell">
  <nav class="tab-bar">
    <span class="tab active">Home</span>
    <span class="tab" style="left:96px">Knowledge Base</span>
    <span class="tab" style="left:224px">Create a Ticket</span>
    <span class="tab" style="left:344px">Check Existing Ticket</span>
    <div class="search">Search Knowledgebase...</div>
  </nav>

  <section class="support-panel">
    <div class="panel-head">
      <h1>BrindleQuay.com Suport Desk</h1>
      <p>Below You'll find instructions for accessing the main areas of our support desk.</p>
    </div>
    <div class="options-card">
      <div class="agent-photo" role="img" aria-label="Smiling support agent wearing a headset, arms folded"></div>
      <div class="option question">
        <div class="pill">Do you have a question ?</div>
        <p>Simply submit a ticket and one of our suport representatives wil be in touch shortly to help you.</p>
        <div class="btn">Create a Ticket</div>
      </div>
      <div class="option ticket">
        <div class="pill">Do you have an existing ticket ?</div>
        <p>No problem, You can see the status, check for updates, and read all of your existing tickets.</p>
        <div class="btn">Check Existing Ticket</div>
      </div>
    </div>
  </section>
</main>

<footer>
  <ul class="footer-links" style="left:161px"><li>Home</li><li>How it Works</li><li>Why Us</li><li>Why Host</li><li>Videos</li></ul>
  <ul class="footer-links" style="left:313px"><li>Plan Your Holiday</li><li>Our Elite Spaces</li><li>Bonus</li></ul>
  <ul class="footer-links" style="left:464px"><li>Terms &amp; Condtion</li><li>Privacy Policy</li><li>Guest Refund Policy</li><li>Feedback And Extortion Policy</li><li>Host Obligations</li></ul>
  <div class="social-title">Join Us on :</div>
  <span class="social" style="left:660px"></span>
  <span class="social" style="left:693px"></span>
  <span class="social" style="left:727px"></span>
  <svg class="to-top" width="24" height="24" viewBox="0 0 24 24"><circle cx="12" cy="12" r="11" fill="#666"/><path d="M6.5 15 L12 8.5 L17.5 15 Z" fill="#fff"/></svg>

  <div class="contact-band">
    <svg width="18" height="22" viewBox="0 0 18 22"><rect x="1" y="1" width="16" height="20" rx="2" fill="#ddd"/><rect x="4" y="3" width="10" height="5" fill="#4a4a4a"/><g fill="#4a4a4a"><rect x="4" y="10" width="2.5" height="2"/><rect x="7.8" y="10" width="2.5" height="2"/><rect x="11.5" y="10" width="2.5" height="2"/><rect x="4" y="14" width="2.5" height="2"/><rect x="7.8" y="14" width="2.5" height="2"/><rect x="11.5" y="14" width="2.5" height="2"/></g></svg>
    <span><b>Questions?</b> <a href="#">Contact our friendly sales team</a> and we'll explain it all to you !</span>
  </div>
  <div class="copyright">Copyright © 2013 <b>BrindleQuay.Com</b>. All rights reserved.</div>
</footer>
</body>
</html>
```